New more attractive design for an old tired look that is high tech but inviting

Need a more modern eye catching design. We are and I/T and MSP and we need a new look. Need a call to action on each page. Needs to be in WordPress. Existing site is quorbelna.com. Needs to work on phones and tablets. The default home page should present us as an MSP/MSSP and direct the viewer to our services we offer.
Updates

Current deadline assigned at project inception has passed before project started

Need extra days to review

Target Market(s)

Our target market is other businesses. We do not target residential customers.

Industry/Entity Type

Business to Business oriented

Coding

Coded - Design and coding required

Number of Pages Required

5+ page

Font styles to use
Sans Serif

Requirements
Must have
• Must have a current relevant design with a call to action on each page.
Nice to have
• Dark background high tech look with people to make it attractive

```html
<!DOCTYPE html>
<html lang="en">
<head>
<meta charset="utf-8">
<title>Data Center Services | Quorbelna</title>
<link href="https://fonts.googleapis.com/css2?family=Arimo:wght@400;700&family=Poppins:wght@400;500;600;700&display=swap" rel="stylesheet">
<style>
:root{
  --blue:#0a69c7;
  --blue-dark:#0e58a6;
  --red:#dc1f26;
  --ink:#333a44;
  --white:#ffffff;
  --band:#d7e2ec;
}
*{box-sizing:border-box;margin:0;padding:0}
html,body{width:823px;height:1200px;overflow:hidden;background:var(--white)}
body{position:relative;font-family:"Poppins",sans-serif;color:var(--ink)}
.site-header{position:absolute;top:6px;left:0;width:823px;height:47px;background:var(--blue)}
.brand{position:absolute;left:72px;top:9px;color:var(--white);font-family:"Arimo",sans-serif;font-weight:700;font-size:21px;letter-spacing:.2px;display:flex;align-items:center;gap:6px}
.brand-mark{width:9px;height:9px;background:var(--red)}
.main-nav{position:absolute;left:0;top:0;height:47px;width:823px}
.main-nav a{position:absolute;top:0;height:47px;line-height:47px;color:var(--white);font-family:"Arimo",sans-serif;font-weight:700;font-size:11px;text-decoration:none;text-align:center}
.nav-services{left:336px;width:90px}
.nav-about{left:427px;width:82px;border-left:1px solid rgba(255,255,255,.15);border-right:1px solid rgba(255,255,255,.15)}
.nav-contact{left:510px;width:102px}
.nav-phone{left:612px;width:128px;background:var(--red);display:flex;align-items:center;justify-content:center;gap:5px}
.hero{position:absolute;top:53px;left:0;width:823px;height:339px;text-align:center;
  background:linear-gradient(180deg,#d4dee8 0%,#f4f5f6 18%,#f7f7f7 30%,#6f5b73 48%,#4a3a52 68%,#f0b7ae 78%,#3b2f45 100%)}
.hero-copy{position:absolute;top:0;left:0;width:100%;background:linear-gradient(180deg,#d6e0ea 0%,#f7f7f7 60%,rgba(247,247,247,0) 100%);height:140px}
.hero h1{position:absolute;top:23px;width:100%;font-size:20px;font-weight:600;color:var(--blue-dark)}
.hero p{position:absolute;top:54px;left:220px;width:383px;font-size:9px;line-height:14px;color:#444}
.btn{display:block;background:var(--red);color:var(--white);font-family:"Arimo",sans-serif;font-weight:700;text-decoration:none;text-align:center}
.hero .btn{position:absolute;left:358px;top:95px;width:110px;height:31px;line-height:31px;border-radius:7px;font-size:10.5px}
.features-intro{position:absolute;top:424px;width:823px;text-align:center}
.features-intro h2{font-size:18.5px;font-weight:600;color:var(--blue)}
.features-intro p{margin-top:8px;font-size:11px;color:#333}
.feature{position:absolute;top:506px;width:214px;height:248px;border-radius:15px;background:var(--blue);color:var(--white);text-align:center;padding:28px 14px 0}
.feature--red{background:var(--red)}
.feature svg{display:block;margin:0 auto;height:52px;width:62px}
.feature h3{margin-top:20px;font-family:"Arimo",sans-serif;font-size:15px;font-weight:700}
.feature p{margin-top:13px;font-size:9px;line-height:14px}
.f1{left:70px}.f2{left:297px}.f3{left:524px}
.promo{position:absolute;top:792px;left:0;width:823px;height:279px;background:var(--band)}
.promo-art{position:absolute;left:164px;top:22px;width:498px;height:166px;border-radius:40px;
  background:radial-gradient(ellipse at 50% 60%,#4a5a78 0%,#8b9fb8 40%,rgba(215,226,236,0) 72%)}
.promo .btn{position:absolute;left:246px;top:202px;width:334px;height:45px;line-height:45px;border-radius:9px;font-family:"Poppins",sans-serif;font-weight:600;font-size:15.5px;letter-spacing:-.2px}
.site-footer{position:absolute;top:1071px;left:0;width:823px;height:121px;background:var(--blue);color:var(--white);text-align:center}
.footer-nav{margin-top:28px;font-size:10.5px;font-weight:600}
.footer-nav a{color:var(--white);text-decoration:none}
.footer-nav span{margin:0 7px}
.legal{margin-top:13px;font-size:10px;line-height:20px}
.legal b{font-weight:600}
</style>
</head>
<body>
<header class="site-header">
  <div class="brand"><span class="brand-mark"></span>Quorbelna</div>
  <nav class="main-nav">
    <a class="nav-services" href="#">SERVICES</a>
    <a class="nav-about" href="#">ABOUT</a>
    <a class="nav-contact" href="#">CONTACT</a>
    <a class="nav-phone" href="#"><svg width="12" height="12" viewBox="0 0 24 24"><path d="M6.6 10.8a15 15 0 0 0 6.6 6.6l2.2-2.2c.3-.3.7-.4 1-.2 1.1.4 2.3.6 3.6.6.6 0 1 .4 1 1V20c0 .6-.4 1-1 1A17 17 0 0 1 3 4c0-.6.4-1 1-1h3.5c.6 0 1 .4 1 1 0 1.3.2 2.5.6 3.6.1.3 0 .7-.2 1z" fill="#fff"/></svg>555-014-2870</a>
  </nav>
</header>

<section class="hero" role="img" aria-label="Illustration of a data center aisle lined with server racks">
  <div class="hero-copy"></div>
  <h1>Data Center Services</h1>
  <p>We offer colocation, virtualization, storage as a service and disaster recovery out of our own enterprise-grade data center.</p>
  <a class="btn" href="#">READ MORE</a>
</section>

<section class="features-intro">
  <h2>Your Data Center, Your Way</h2>
  <p>From single colocated servers to fully redundant virtualized environments.</p>
</section>

<article class="feature f1">
  <svg viewBox="0 0 62 52" fill="none" stroke="#fff" stroke-width="2" stroke-linejoin="round" stroke-linecap="round"><path d="M3 14l10-8 8 5M59 14L49 6l-9 6-12 8c-2 2 0 5 3 4l9-5"/><path d="M13 6l-8 16 16 18c2 2 5 0 4-2M21 40l4 4c2 2 5 0 4-2M29 42l2 2c2 2 5-1 3-3M49 6l8 16-15 16"/><path d="M15 32l4-4M19 36l4-4"/></svg>
  <h3>A True Partner</h3>
  <p>One size data center architecture does not fit all. We take the time to understand your specific requirements. We can provide as much or as little expertise as your organization requires for your specific project.</p>
</article>
<article class="feature feature--red f2">
  <svg viewBox="0 0 62 52" fill="none" stroke="#fff" stroke-width="2" stroke-linejoin="round" stroke-linecap="round"><path d="M31 1l21 8v14c0 14-9 23-21 28C19 46 10 37 10 23V9z"/><path d="M31 6l16 6v11c0 11-7 18-16 22-9-4-16-11-16-22V12z"/><path d="M22 26l7 7 12-13"/></svg>
  <h3>High Security</h3>
  <p>Our data center is a Tier III, standalone structure designed to withstand wind speeds up to 206mph. We have fully redundant power, cooling and internet connectivity. Biometrics are required to enter and visitors are always escorted.</p>
</article>
<article class="feature f3">
  <svg viewBox="0 0 62 52" fill="none" stroke="#fff" stroke-width="2" stroke-linejoin="round" stroke-linecap="round"><circle cx="35" cy="17" r="10"/><path d="M35 2v4M35 28v4M20 17h4M46 17h4M24 6l3 3M43 25l3 3M46 6l-3 3M27 25l-3 3"/><path d="M30 17l4 4 6-7"/><path d="M6 40l7-7h10l8 4h-9M13 45l4-3h14l14-10c2-1 4 1 3 3L36 48H14"/><path d="M3 39l7 9"/></svg>
  <h3>Availability</h3>
  <p>The facility is powered by two separate utility feeds and an industrial diesel generator. We utilize multiple in-row cooling units, in-rack A/B power feeds and also have redundant, geographically diverse internet paths.</p>
</article>

<section class="promo">
  <div class="promo-art" role="img" aria-label="Illustration of a person with a laptop among cloud storage, servers, a padlock and a security shield"></div>
  <a class="btn" href="#">More About Data Center Services</a>
</section>

<footer class="site-footer">
  <nav class="footer-nav">
    <a href="#">HOME</a><span>|</span><a href="#">SERVICES</a><span>|</span><a href="#">ABOUT</a><span>|</span><a href="#">CONTACT</a><span>|</span><a href="#">PRIVACY POLICY</a><span>|</span><a href="#">TERMS &amp; CONDITIONS</a>
  </nav>
  <div class="legal">
    2025 © QUORBELNA NETWORKS, INC.<br>
    418 RIDGEWAY DR | ALDER FALLS, SC 29600 &nbsp;&nbsp;&nbsp;›&nbsp;&nbsp;&nbsp; <b>OFFICE:</b> (555) 014-2870
  </div>
</footer>
</body>
</html>
```